Overview of Elder Abuse Resources Brochure

We need a 2-page brochure that provides a list of resources for elders in tribal communities in the US and those who care for them. We want it to be simple and easy to read, and easy to see the difference between each resource. We would also like eye-catching images or graphics. Please keep the images on the front, and add any photos or graphics that depict Native American elders. We need both of our logos on the first page, in the far-right column. Please refer to the attached image for our brand colors and a font suggestion. Please keep the three columns on each page, but delete the blank pages in the document.

```html
<!DOCTYPE html>
<html lang="en">
<head>
<meta charset="utf-8">
<title>Elder Resources Brochure</title>
<link href="https://fonts.googleapis.com/css2?family=Barlow+Condensed:wght@500;600;700&family=Oswald:wght@500&family=Rubik:wght@400;500;700&display=swap" rel="stylesheet">
<style>
:root{
  --bg:#5b5b5b;
  --teal:#52aab4;
  --teal-dark:#2f7d87;
  --teal-light:#b9dfe3;
  --rust:#b3584d;
  --rust-dark:#9a463e;
  --cream:#f3eeea;
  --cream-2:#efe8e2;
  --white:#ffffff;
  --ink:#2a2a2a;
  --head:"Barlow Condensed",sans-serif;
  --body:"Rubik",sans-serif;
}
*{box-sizing:border-box;margin:0;padding:0}
html,body{width:1035px;height:1200px;overflow:hidden;background:var(--bg)}
body{position:relative;font-family:var(--body);color:var(--ink)}
.section-label{position:absolute;font-family:"Oswald",sans-serif;font-weight:500;color:#fff;font-size:15px;letter-spacing:7px}
.sheet{position:absolute;overflow:hidden}
.abs{position:absolute}
.bg-svg{position:absolute;left:0;top:0}
.vert{position:absolute;writing-mode:vertical-rl;transform:rotate(180deg);font-size:8.6px;line-height:10.5px;color:#222;white-space:nowrap}
.vert b{font-weight:700}
.vert-logo{position:absolute;writing-mode:vertical-rl;transform:rotate(180deg);font-family:var(--head);font-weight:600;color:var(--teal-dark);font-size:11px;line-height:11px;text-transform:uppercase;white-space:nowrap}
.chevron-band{position:absolute;height:23px;background:var(--teal-light)}

/* Front panel */
.front-panel{position:absolute;top:45px;width:234px;height:533px;background:var(--cream);overflow:hidden}
.logo-pair{position:absolute;top:26px;left:0;width:234px;height:50px}
.logo-name{position:absolute;top:8px;width:90px;text-align:center;font-family:var(--head);font-weight:600;font-size:14px;line-height:15px;text-transform:uppercase;color:var(--teal-dark)}
.logo-name.left{left:20px}
.logo-name.right{left:126px}
.logo-divider{position:absolute;left:117px;top:0;width:1px;height:50px;background:#c9bcb4}
.front-title{position:absolute;top:97px;left:0;width:234px;text-align:center;font-family:var(--head);font-weight:600;line-height:19px}
.front-title .t1{display:block;color:var(--teal-dark);font-size:16px}
.front-title .t2{display:block;color:var(--rust);font-size:19px}
.who-list{position:absolute;left:20px;top:190px;list-style:none;color:#fff;font-size:9.6px;font-weight:500;line-height:13.8px}
.who-list li::before{content:"• "}
.ask-btn{position:absolute;top:413px;height:32px;border-radius:7px;color:#fff;font-size:7.2px;font-weight:500;line-height:9px;text-align:center;display:flex;align-items:center;justify-content:center;padding:0 4px}
.ask-btn.left{left:10px;width:98px;background:var(--teal-dark)}
.ask-btn.right{left:116px;width:102px;background:var(--rust)}
.bulb{position:absolute;top:396px;width:24px;height:24px;border-radius:50%;border:2px solid #fff;display:flex;align-items:center;justify-content:center}
.front-note{position:absolute;top:453px;left:0;width:234px;text-align:center;color:#fff;font-size:10.2px;font-weight:500;line-height:12.5px}

/* Outside left */
.respect-title{position:absolute;left:24px;top:147px;font-family:var(--head);font-weight:700;font-size:19px;color:var(--rust);letter-spacing:.2px}
.respect-copy{position:absolute;left:24px;width:190px;font-size:8.9px;line-height:11.2px;color:#222}
.respect-copy strong{font-weight:700}
.help-pill{position:absolute;background:var(--rust);color:#fff;font-family:var(--head);font-weight:600;font-size:12.5px;border-radius:10px;display:flex;align-items:center;padding-left:16px}
.help-box{position:absolute;background:var(--teal-dark);color:#fff}
.contact-lines{position:absolute;font-size:8.1px;line-height:10px;color:#fff}
.contact-lines .phone{font-weight:700;font-size:11.2px;line-height:14px;display:block;margin-top:1px}
.contact-lines .em{font-weight:700;font-size:8.6px;display:block;margin:5px 0 6px}
.contact-lines .gap{display:block;height:7px}

/* Inside */
.stories-card{position:absolute;left:16px;top:16px;width:210px;height:340px;background:var(--cream);border-radius:12px 12px 0 0}
.stories-title{position:absolute;left:16px;top:12px;font-family:var(--head);font-weight:600;font-size:17.5px;line-height:18px;color:var(--teal);text-transform:uppercase}
.story{position:absolute;left:63px;width:132px;font-size:8.7px;line-height:10.8px;color:#2a2a2a}
.story-icon{position:absolute;left:13px;width:43px;height:43px;border-radius:50%;background:var(--rust);border:3px solid #fff;box-shadow:0 0 0 1px #d8b3ad}
.story-rule{position:absolute;left:63px;width:131px;border-top:1px dashed #b9a9a2}
.inside-contact{position:absolute;left:16px;top:340px;width:210px;height:135px;background:var(--rust);border-radius:0 0 12px 12px;overflow:hidden}
.inside-contact .strip{position:absolute;left:0;top:0;width:29px;height:135px;background:var(--rust-dark)}
.strip-label{position:absolute;left:7px;bottom:14px;writing-mode:vertical-rl;transform:rotate(180deg);font-family:var(--head);font-weight:600;font-size:13px;color:#fff;white-space:nowrap}
.col-pill{position:absolute;top:18px;height:22px;border-radius:11px;background:var(--rust-dark);color:#fff;font-family:var(--head);font-weight:600;font-size:13px;display:flex;align-items:center;padding-left:13px;text-transform:uppercase}
.res-card{position:absolute;background:#fff;border:1.2px solid var(--rust);border-radius:7px;padding:6px 8px 0 13px;font-size:7.4px;line-height:9.2px;color:#2a2a2a}
.res-card h3{font-family:var(--head);font-weight:500;font-size:11.6px;line-height:13px;margin-bottom:2px}
.res-card h3.r{color:var(--rust)}
.res-card h3.t{color:var(--teal)}
.res-card .lbl{color:var(--rust);font-weight:500}
.res-card .link{color:var(--rust)}
.sub-head{position:absolute;font-family:var(--head);font-weight:600;font-size:12.5px;color:var(--rust);text-transform:uppercase}
.sub-note{position:absolute;font-family:var(--head);font-weight:500;font-size:10.6px;line-height:13px;color:#2a2a2a}
.small-icon{position:absolute;width:14px;height:14px;border-radius:50%;border:1.3px solid var(--rust)}
.foot-logo{position:absolute;left:504px;top:484px;font-family:var(--head);font-weight:600;font-size:11px;line-height:11px;color:var(--teal-dark);text-transform:uppercase;display:flex;align-items:center;gap:6px}
.foot-logo .dot{width:12px;height:12px;border-radius:50%;background:var(--teal-dark)}
</style>
</head>
<body>

<div class="section-label" style="left:347px;top:20px">OUTSIDE</div>
<div class="section-label" style="left:838px;top:20px">COVER</div>
<div class="section-label" style="left:347px;top:594px">INSIDE</div>
<div class="section-label" style="left:838px;top:594px">BACK</div>

<!-- OUTSIDE SPREAD: left panel -->
<section class="sheet outside-left" style="left:50px;top:45px;width:226px;height:533px;background:#fff">
  <svg class="bg-svg" width="226" height="533" viewBox="0 0 226 533">
    <path d="M226,278 C196,320 180,380 172,440 L160,533 L226,533 Z" fill="var(--teal)"/>
    <path d="M60,127 Q150,133 226,112 L226,121 Q150,141 60,127 Z" fill="var(--teal)"/>
  </svg>
  <svg class="bg-svg" width="226" height="130" viewBox="0 0 226 130" role="img" aria-label="Photo of a group of smiling Native American elders outdoors">
    <defs><linearGradient id="groupPhoto" x1="0" y1="0" x2="0" y2="1"><stop offset="0" stop-color="#4f6b3e"/><stop offset=".55" stop-color="#8a6b5e"/><stop offset="1" stop-color="#c9b49d"/></linearGradient></defs>
    <path d="M0,0 H226 V112 Q150,132 60,126 Q28,123 0,113 Z" fill="url(#groupPhoto)"/>
  </svg>
  <h2 class="respect-title">RESPECT FOR ELDERS</h2>
  <p class="respect-copy" style="top:173px">Do you have concerns about an Elder, maybe you see that they are not taking care of themselves, or family only comes once a month when the Elder has money?</p>
  <p class="respect-copy" style="top:240px">Is an Elder telling you that they are not treated with respect or that someone is bothering them?</p>
  <p class="respect-copy" style="top:286px;font-size:9.2px"><strong>These may be signs of Elder abuse, neglect or exploitation.</strong></p>
  <div class="help-box" style="left:23px;top:333px;width:181px;height:146px"></div>
  <div class="help-pill" style="left:18px;top:323px;width:150px;height:21px">FOR HELP CONTACT:</div>
  <div class="contact-lines" style="left:34px;top:357px;width:165px">
    Elder Help Finder for information<br>on Adult Protective Services
    <span class="phone">1-800-555-0142</span>
    <span class="em">If a serious emergency, call 911.</span>
    For mental health support for yourself<br>or an Elder, <b>call or text 555</b>
    <span class="gap"></span>
    Family Safety Hotline
    <span class="phone">1.800.555.0177</span>
  </div>
  <div class="chevron-band" role="img" aria-label="White chevron pattern band" style="left:0;top:495px;width:226px"></div>
</section>

<!-- OUTSIDE SPREAD: mailing panel -->
<section class="sheet mailing" style="left:276px;top:45px;width:225px;height:533px;background:#fff">
  <div class="vert" style="left:95px;bottom:184px"><b>Recipient</b><br>Street Address<br>City, ST ZIP Code</div>
  <div class="vert" style="left:23px;bottom:15px">Company Name<br>Street Address<br>City, ST ZIP</div>
  <div class="vert" style="left:192px;bottom:171px">Website<br>Email</div>
  <div class="vert" style="left:192px;bottom:15px">Tel Telephone<br>Fax Fax</div>
  <div class="vert-logo" style="left:191px;top:26px">Council for<br>Native Elder Care</div>
</section>

<!-- FRONT PANEL (outside right) -->
<section class="front-panel" style="left:501px">
  <svg class="bg-svg" width="234" height="533" viewBox="0 0 234 533">
    <rect x="0" y="300" width="234" height="233" fill="var(--teal)"/>
    <path d="M0,155 Q117,136 234,170 L234,186 Q117,150 0,168 Z" fill="var(--rust)"/>
  </svg>
  <svg class="bg-svg" width="234" height="533" viewBox="0 0 234 533" role="img" aria-label="Photo of two Native American elder women in traditional dress and jewelry">
    <defs><linearGradient id="elderPhotoA" x1="0" y1="0" x2="1" y2="1"><stop offset="0" stop-color="#241a1f"/><stop offset=".5" stop-color="#6b2346"/><stop offset="1" stop-color="#8c3a5a"/></linearGradient></defs>
    <path d="M0,168 Q117,150 234,186 L234,330 Q160,400 70,375 Q30,362 0,340 Z" fill="url(#elderPhotoA)"/>
    <path d="M0,345 Q40,368 80,380 Q165,402 234,336" fill="none" stroke="#fff" stroke-width="2"/>
  </svg>
  <div class="logo-pair">
    <div class="logo-name left">Native Elder<br>Council</div>
    <div class="logo-divider"></div>
    <div class="logo-name right" style="color:var(--rust)">Elder Justice<br>Circle</div>
  </div>
  <h1 class="front-title"><span class="t1">Services for Elders &amp;</span><span class="t2">People Who Care for Them</span></h1>
  <ul class="who-list"><li>My Mother</li><li>My Father</li><li>My Sister</li><li>My Grandchild</li><li>Myself</li></ul>
  <div class="bulb" style="left:47px;background:var(--teal-dark)"><svg width="12" height="14" viewBox="0 0 12 14"><path d="M6,1 A4.5,4.5 0 0 1 8.5,9.2 V11 H3.5 V9.2 A4.5,4.5 0 0 1 6,1 Z M4,12.3 H8" fill="none" stroke="#fff" stroke-width="1.2"/></svg></div>
  <div class="bulb" style="left:154px;background:var(--rust)"><svg width="12" height="14" viewBox="0 0 12 14"><path d="M6,1 A4.5,4.5 0 0 1 8.5,9.2 V11 H3.5 V9.2 A4.5,4.5 0 0 1 6,1 Z M4,12.3 H8" fill="none" stroke="#fff" stroke-width="1.2"/></svg></div>
  <div class="ask-btn left">Are you caring for an<br>Elder or a Grandchild?</div>
  <div class="ask-btn right">Are you an Elder who needs<br>help staying at home?</div>
  <p class="front-note">These programs and information can<br>be a helpful resource.</p>
  <div class="chevron-band" role="img" aria-label="White chevron pattern band" style="left:0;top:495px;width:234px"></div>
</section>

<!-- COVER -->
<section class="front-panel" style="left:756px">
  <svg class="bg-svg" width="234" height="533" viewBox="0 0 234 533">
    <rect x="0" y="300" width="234" height="233" fill="var(--teal)"/>
    <path d="M0,155 Q117,136 234,170 L234,186 Q117,150 0,168 Z" fill="var(--rust)"/>
  </svg>
  <svg class="bg-svg" width="234" height="533" viewBox="0 0 234 533" role="img" aria-label="Photo of two Native American elder women in traditional dress and jewelry">
    <defs><linearGradient id="elderPhotoB" x1="0" y1="0" x2="1" y2="1"><stop offset="0" stop-color="#241a1f"/><stop offset=".5" stop-color="#6b2346"/><stop offset="1" stop-color="#8c3a5a"/></linearGradient></defs>
    <path d="M0,168 Q117,150 234,186 L234,330 Q160,400 70,375 Q30,362 0,340 Z" fill="url(#elderPhotoB)"/>
    <path d="M0,345 Q40,368 80,380 Q165,402 234,336" fill="none" stroke="#fff" stroke-width="2"/>
  </svg>
  <div class="logo-pair">
    <div class="logo-name left">Native Elder<br>Council</div>
    <div class="logo-divider"></div>
    <div class="logo-name right" style="color:var(--rust)">Elder Justice<br>Circle</div>
  </div>
  <h1 class="front-title"><span class="t1">Services for Elders &amp;</span><span class="t2">People Who Care for Them</span></h1>
  <ul class="who-list"><li>My Mother</li><li>My Father</li><li>My Sister</li><li>My Grandchild</li><li>Myself</li></ul>
  <div class="bulb" style="left:47px;background:var(--teal-dark)"><svg width="12" height="14" viewBox="0 0 12 14"><path d="M6,1 A4.5,4.5 0 0 1 8.5,9.2 V11 H3.5 V9.2 A4.5,4.5 0 0 1 6,1 Z M4,12.3 H8" fill="none" stroke="#fff" stroke-width="1.2"/></svg></div>
  <div class="bulb" style="left:154px;background:var(--rust)"><svg width="12" height="14" viewBox="0 0 12 14"><path d="M6,1 A4.5,4.5 0 0 1 8.5,9.2 V11 H3.5 V9.2 A4.5,4.5 0 0 1 6,1 Z M4,12.3 H8" fill="none" stroke="#fff" stroke-width="1.2"/></svg></div>
  <div class="ask-btn left">Are you caring for an<br>Elder or a Grandchild?</div>
  <div class="ask-btn right">Are you an Elder who needs<br>help staying at home?</div>
  <p class="front-note">These programs and information can<br>be a helpful resource.</p>
  <div class="chevron-band" role="img" aria-label="White chevron pattern band" style="left:0;top:495px;width:234px"></div>
</section>

<!-- INSIDE SPREAD -->
<section class="sheet inside" style="left:50px;top:619px;width:686px;height:533px;background:#fbfaf9">
  <svg class="bg-svg" width="686" height="533" viewBox="0 0 686 533">
    <rect x="460" y="0" width="226" height="533" fill="var(--cream-2)"/>
    <path d="M0,0 H378 C330,40 300,90 288,150 L280,533 H0 Z" fill="var(--teal)"/>
    <path d="M0,505 H320 L340,533 H0 Z" fill="var(--teal)"/>
    <line x1="460" y1="0" x2="460" y2="533" stroke="#e3dcd6" stroke-width="1"/>
  </svg>
  <div class="chevron-band" role="img" aria-label="White chevron pattern band" style="left:0;top:495px;width:330px;background:#d3ecee"></div>

  <div class="stories-card">
    <h2 class="stories-title">Do these stories sound<br>familiar to you?</h2>
    <div class="story-icon" style="top:58px"></div>
    <p class="story" style="top:68px">My mother gets lost driving home from the store.</p>
    <div class="story-rule" style="top:101px"></div>
    <div class="story-icon" style="top:103px"></div>
    <p class="story" style="top:113px">I need help getting groceries and with chores at home.</p>
    <div class="story-rule" style="top:143px"></div>
    <div class="story-icon" style="top:151px"></div>
    <p class="story" style="top:154px">My dad wants to sleep all the time; he doesn’t go out with friends anymore. He stopped drumming</p>
    <div class="story-rule" style="top:204px"></div>
    <div class="story-icon" style="top:199px"></div>
    <p class="story" style="top:213px">My sister is raising 3 grandchildren on her own.</p>
    <div class="story-rule" style="top:243px"></div>
    <div class="story-icon" style="top:250px"></div>
    <p class="story" style="top:253px">My son is disrespecting me. He only comes to visit when my retirement money arrives. He always asks for money.</p>
  </div>
  <div class="inside-contact">
    <div class="strip"><div class="strip-label">FOR HELP CONTACT:</div></div>
    <div class="contact-lines" style="left:44px;top:12px;width:160px">
      Elder Help Finder for information<br>on Adult Protective Services
      <span class="phone">1-800-555-0142</span>
      <span class="em">If a serious emergency, call 911.</span>
      For mental health support for yourself<br>or an Elder, <b>call or text 555</b>
      <span class="gap"></span>
      Family Safety Hotline
      <span class="phone">1.800.555.0177</span>
    </div>
  </div>

  <!-- Resources for elders -->
  <div class="col-pill" style="left:252px;width:190px">Resources for Elders</div>
  <div class="res-card" style="left:256px;top:50px;width:183px;height:80px">
    <h3 class="r">Elder Help Finder</h3>
    https://elderhelpfinder.example.org<br>
    <span class="lbl">Call or Text:</span> 1-800-555-0142<br>
    <span class="lbl">Email:</span> help@elderhelpfinder.example.org<br>
    For help finding support. Ask about services to Tribal Elders.
  </div>
  <div class="res-card" style="left:256px;top:137px;width:183px;height:97px">
    <h3 class="t">Memory Care Support Line</h3>
    (24 hours 7 days a week)<br>
    <span class="lbl">Call:</span> 1-800-555-0178<br>
    For support for people living with dementia, caregivers, families and the public. Connect with a live person who can provide information, local resources, crisis assistance and emotional support.
  </div>
  <div class="res-card" style="left:256px;top:242px;width:183px;height:62px">
    <h3 class="r">555 Crisis Support Line</h3>
    (24 hours 7 days a week)<br>
    <span style="display:block;height:4px"></span>
    For mental health support,<br><span class="lbl" style="font-weight:700">call or text 555.</span>
  </div>
  <div class="res-card" style="left:256px;top:312px;width:183px;height:93px">
    <h3 class="t">State &amp; Tribal Hotlines | Elder Justice Circle</h3>
    To find local resources within your tribe or state that specialize in elder abuse, neglect or exploitation, visit:<br>
    <span class="link">https://elderjusticecircle.example.org/hotlines/state-tribal/</span>
  </div>
  <div class="res-card" style="left:256px;top:413px;width:183px;height:89px">
    <h3 class="r">Sacred Circle Helpline</h3>
    A 24/7 safe, confidential and anonymous domestic and sexual violence helpline for Native Americans and Alaska Natives.<br>
    <span class="lbl">Call</span> 1-844-555-0163<br>
    <span class="link">(1-844-555-HELP)</span><br>
    <span class="link">https://sacredcirclehelpline.example.org/</span>
  </div>

  <!-- Resources for caregivers -->
  <div class="col-pill" style="left:482px;width:190px">Resources for Caregivers</div>
  <div class="small-icon" style="left:487px;top:47px"></div>
  <div class="sub-head" style="left:506px;top:47px">Caring for an Older Adult</div>
  <div class="res-card" style="left:486px;top:68px;width:183px;height:81px">
    <h3 class="r">Elder Help Finder</h3>
    https://elderhelpfinder.example.org<br>
    <span class="lbl">Call or Text:</span> 1-800-555-0142<br>
    <span class="lbl">Email:</span> help@elderhelpfinder.example.org<br>
    For help finding support. Ask about services to Tribal Elders
  </div>
  <div class="res-card" style="left:486px;top:156px;width:183px;height:83px">
    <h3 class="t">Memory Friends | Council for Native Elder Care</h3>
    An interactive educational program to better understand what dementia is and how it affects people.<br>
    <span class="link">https://nativeeldercare.example.org/memory-friends/</span>
  </div>
  <div class="small-icon" style="left:487px;top:250px"></div>
  <div class="sub-head" style="left:512px;top:248px">Caring for a Grandchild</div>
  <div class="sub-note" style="left:512px;top:263px">Grandparents Raising Grandchildren<br>(Kinship Care)</div>
  <div class="res-card" style="left:486px;top:296px;width:183px;height:62px">
    <h3 class="r">KinshipFamilies.example</h3>
    An interactive website that seeks to share all relevant publicly available information impacting grandfamilies
  </div>
  <div class="res-card" style="left:486px;top:367px;width:183px;height:83px">
    <h3 class="t">Grandparent Resources | Elder Justice Circle</h3>
    A list of resources for grandparents raising grandchildren<br>
    <span class="link">https://elderjusticecircle.example.org/grandparent-resources/</span>
  </div>
  <div class="foot-logo"><span class="dot"></span><span>Council for<br>Native Elder Care</span></div>
</section>

<!-- BACK -->
<section class="sheet mailing back" style="left:756px;top:618px;width:226px;height:533px;background:#fff">
  <div class="vert" style="left:95px;bottom:184px"><b>Recipient</b><br>Street Address<br>City, ST ZIP Code</div>
  <div class="vert" style="left:23px;bottom:15px">Company Name<br>Street Address<br>City, ST ZIP</div>
  <div class="vert" style="left:193px;bottom:170px">Website<br>Email</div>
  <div class="vert" style="left:193px;bottom:15px">Tel Telephone<br>Fax Fax</div>
  <div class="vert-logo" style="left:192px;top:26px">Council for<br>Native Elder Care</div>
</section>

</body>
</html>
```